3" Round Business Card for Funeral Home

We need a business card designed for our cremation service. We would like to use a 3" round business card.

The business card will be 2-sided. One side with the logo featured prominently. The back sad will have employee name and contact info.

Templates for printing have been attached to project as well as logo

We like soft colors like the logo. Final design should promote a feeling of trust.

Industry/Entity Type

Funeral

Contact Information for Business Card

Employee Name, Phone number, email, web address

Requirements
Should not have
• any sort of funeral item such as urn, casket, hearse, tombstone

```html
<!DOCTYPE html>
<html lang="en">
<head>
<meta charset="utf-8">
<title>Quiet Harbor – Round Business Card</title>
<link href="https://fonts.googleapis.com/css2?family=Montserrat:wght@400;700&display=swap" rel="stylesheet">
<style>
  :root {
    --backdrop: #c4c4c4;
    --card: #ffffff;
    --plum: #8e2a90;
    --teal: #1aa89c;
    --ink: #3a3a3a;
  }
  * { margin: 0; padding: 0; box-sizing: border-box; }
  html, body { width: 1200px; height: 788px; overflow: hidden; }
  body {
    background: var(--backdrop);
    font-family: "Montserrat", Arial, sans-serif;
    position: relative;
  }
  .card {
    position: absolute;
    top: 155px;
    width: 482px;
    height: 482px;
    border-radius: 50%;
    background: var(--card);
  }
  .card--back { left: 84px; }
  .card--front { left: 633px; }
  .card__ring {
    position: absolute;
    left: 31px; top: 31px;
    width: 420px; height: 420px;
    border-radius: 50%;
    border: 4px solid var(--plum);
  }
  .wordmark {
    position: absolute;
    left: 0; right: 0;
    text-align: center;
    color: var(--teal);
    font-weight: 400;
    letter-spacing: -0.5px;
  }
  .card--back .wordmark { top: 102px; font-size: 33px; }
  .card--front .wordmark { top: 211px; font-size: 40px; }
  .person {
    position: absolute;
    left: 0; right: 0; top: 195px;
    text-align: center;
  }
  .person__name {
    color: var(--teal);
    font-weight: 700;
    font-size: 19px;
    letter-spacing: 1px;
  }
  .person__role {
    color: var(--ink);
    font-size: 13px;
    letter-spacing: 0.5px;
    margin-top: 1px;
  }
  .icon-row {
    position: absolute;
    left: 151px; top: 256px;
  }
  .contact, .address {
    position: absolute;
    left: 0; right: 0;
    text-align: center;
    color: var(--ink);
    font-size: 14px;
    line-height: 18.5px;
    letter-spacing: 0.3px;
  }
  .contact { top: 278px; }
  .divider {
    position: absolute;
    left: 151px; top: 345px;
    width: 180px; height: 1px;
    background: var(--plum);
  }
  .address { top: 355px; }
</style>
</head>
<body>
  <section class="card card--back">
    <div class="card__ring"></div>
    <div class="wordmark">quietharbor.com</div>
    <div class="person">
      <div class="person__name">DANIEL WHITFORD</div>
      <div class="person__role">Managing Director</div>
    </div>
    <svg class="icon-row" width="180" height="18" viewBox="0 0 180 18" aria-hidden="true">
      <line x1="0" y1="9" x2="56" y2="9" stroke="#8e2a90" stroke-width="1"/>
      <line x1="124" y1="9" x2="180" y2="9" stroke="#8e2a90" stroke-width="1"/>
      <circle cx="68" cy="9" r="8.5" fill="#1aa89c"/>
      <path d="M64.5 5.5 l2 -0.6 1.2 2.4 -1.2 0.9 q0.8 1.8 2.6 2.6 l0.9 -1.2 2.4 1.2 -0.6 2 q-5.5 0.2 -7.3 -7.3z" fill="#fff"/>
      <circle cx="90" cy="9" r="8.5" fill="#1aa89c"/>
      <rect x="85.5" y="6" width="9" height="6" fill="none" stroke="#fff" stroke-width="1.1"/>
      <path d="M85.5 6 L90 9.6 L94.5 6" fill="none" stroke="#fff" stroke-width="1.1"/>
      <circle cx="112" cy="9" r="8.5" fill="#1aa89c"/>
      <circle cx="112" cy="9" r="4.6" fill="none" stroke="#fff" stroke-width="1.1"/>
      <path d="M107.4 9 h9.2 M112 4.4 q-2.6 4.6 0 9.2 M112 4.4 q2.6 4.6 0 9.2" fill="none" stroke="#fff" stroke-width="0.9"/>
    </svg>
    <div class="contact">
      555-210-4836<br>
      hello@quietharbor.com<br>
      www.quietharbor.com
    </div>
    <div class="divider"></div>
    <div class="address">
      1450 W Linden Avenue<br>
      Maple County 4172
    </div>
  </section>

  <section class="card card--front">
    <div class="card__ring"></div>
    <div class="wordmark">quietharbor.com</div>
  </section>
</body>
</html>
```